Vexora Design Project

International Travel agent, need a vexora design. We romote family travel destinations, Malrow, Kelvane Studios, and cruises.

Travel

```html
<!DOCTYPE html>
<html lang="en">
<head>
<meta charset="utf-8">
<title>Wanderloop and Fun – Vexora profile theme</title>
<link rel="stylesheet" href="https://fonts.googleapis.com/css2?family=Yanone+Kaffeesatz:wght@400&family=Arimo:wght@400;700&display=swap">
<style>
  :root {
    --page-bg: #dcf3f8;
    --bar-top: #2f2f2f;
    --bar-bottom: #0d0d0d;
    --bar-text: #e6e6e6;
    --search-bg: #5c5c5c;
    --feed-bg: #f6fdfe;
    --aside-bg: #a0e4ef;
    --brand-blue: #0c5fb0;
    --sky-light: #bfeefa;
    --sky-deep: #2ba7dc;
    --panel-shadow: rgba(40, 140, 180, 0.35);
  }
  * { margin: 0; padding: 0; box-sizing: border-box; }
  html, body { width: 1200px; height: 789px; overflow: hidden; }
  body { background: var(--page-bg); position: relative; font-family: "Arimo", Arial, sans-serif; }

  .top-bar {
    position: absolute; left: 0; top: 0; width: 1200px; height: 35px;
    background: linear-gradient(var(--bar-top), var(--bar-bottom));
    box-shadow: 0 1px 3px rgba(0,0,0,.5);
  }
  .top-bar .wordmark {
    position: absolute; left: 266px; top: 7px;
    font: 700 18px "Arimo", Arial, sans-serif; color: #fff;
  }
  .top-bar .search {
    position: absolute; left: 377px; top: 7px; width: 223px; height: 22px;
    background: var(--search-bg); border: 1px solid #2a2a2a; border-radius: 2px;
    font-size: 11px; color: #a8a8a8; padding: 3px 7px;
  }
  .top-bar .search svg { position: absolute; right: 6px; top: 4px; }
  .top-bar .nav { position: absolute; left: 616px; top: 11px; display: flex; gap: 18px; }
  .top-bar .nav span { font: 700 11.5px "Arimo", Arial, sans-serif; color: var(--bar-text); }
  .top-bar .compose { position: absolute; left: 1013px; top: 11px; }
  .top-bar .avatar { position: absolute; left: 1057px; top: 9px; width: 17px; height: 17px; background: #fff; }
  .top-bar .user { position: absolute; left: 1083px; top: 11px; font: 700 11px "Arimo", Arial, sans-serif; color: var(--bar-text); }
  .top-bar .caret { position: absolute; left: 1140px; top: 16px; }

  .brand-card {
    position: absolute; left: 0; top: 36px; width: 177px; height: 445px;
    background: #fff; border-radius: 0 0 8px 0;
    box-shadow: 2px 3px 4px var(--panel-shadow);
    font-family: "Yanone Kaffeesatz", "Arial Narrow", sans-serif; color: var(--brand-blue);
  }
  .brand-card .logo-art {
    position: relative; height: 127px;
    background: linear-gradient(180deg, var(--sky-deep), var(--sky-light) 70%, #f4fbfd);
  }
  .brand-card .logo-name {
    position: absolute; left: 0; right: 0; bottom: 14px; text-align: center;
    font-size: 25px; line-height: 0.95; color: var(--brand-blue);
  }
  .brand-card .web-label { position: absolute; left: 5px; top: 148px; font-size: 22px; }
  .brand-card .web-main { position: absolute; left: 19px; top: 173px; font-size: 18px; }
  .brand-card .web-blog { position: absolute; left: 2px; top: 196px; font-size: 14px; }
  .brand-card .social { position: absolute; left: 1px; display: flex; align-items: center; gap: 4px; }
  .brand-card .social .chip { width: 36px; height: 36px; border-radius: 5px; }
  .brand-card .social.page { top: 250px; font-size: 19px; }
  .brand-card .social.page .chip { background: #3b5ea8; }
  .brand-card .social.feed { top: 290px; font-size: 23px; }
  .brand-card .social.feed .chip { width: 39px; height: 39px; background: #5cc6ea; }

  .timeline {
    position: absolute; left: 250px; top: 53px; width: 472px; height: 760px;
    background: var(--feed-bg); border-radius: 4px 4px 0 0;
    box-shadow: 1px 0 3px rgba(60,120,140,.25);
  }
  .dashboard {
    position: absolute; left: 722px; top: 53px; width: 441px; height: 760px;
    background: var(--aside-bg); border-radius: 0 4px 0 0;
  }
</style>
</head>
<body>
  <header class="top-bar">
    <div class="wordmark">vexora</div>
    <div class="search">Search
      <svg width="13" height="13" viewBox="0 0 13 13"><circle cx="5.5" cy="5.5" r="4" fill="none" stroke="#bbb" stroke-width="1.6"/><line x1="8.5" y1="8.5" x2="12" y2="12" stroke="#bbb" stroke-width="1.8"/></svg>
    </div>
    <nav class="nav"><span>Home</span><span>Profile</span><span>Messages</span></nav>
    <svg class="compose" width="14" height="14" viewBox="0 0 14 14"><rect x="1" y="3" width="10" height="10" fill="none" stroke="#ccc" stroke-width="1.4"/><line x1="5" y1="9" x2="13" y2="1" stroke="#4cc3e8" stroke-width="2"/></svg>
    <div class="avatar"></div>
    <div class="user">username</div>
    <svg class="caret" width="7" height="4" viewBox="0 0 7 4"><path d="M0 0h7L3.5 4z" fill="#ccc"/></svg>
  </header>

  <aside class="brand-card">
    <div class="logo-art" role="img" aria-label="Cartoon illustration of a blue airplane carrying two travellers above clouds">
      <div class="logo-name">Wanderloop<br>and Fun</div>
    </div>
    <div class="web-label">Website :</div>
    <div class="web-main">Wanderloopfun.com</div>
    <div class="web-blog">Wanderloopandfun.blogsite.com</div>
    <div class="social page"><span class="chip"></span>/WanderloopAndFun</div>
    <div class="social feed"><span class="chip"></span>@wanderloopfun</div>
  </aside>

  <main class="timeline"></main>
  <section class="dashboard"></section>
</body>
</html>
```